Cosmetic injections clinic needs a fresh looking business card

We need a business card using the supplied logo and color scheme to attract future clients to our clinic. It should be modern and fresh, eye catching and not too busy. Simple and to the point is best. I would like two sided designs with the front indicating address and contact information, and the back in full color with white logo and descriptive information also provided.
Target Market(s)
Clients looking for non surgical beauty enhancements.
Contact Information for Business Card
MeloraSkin
14, 618 Birchmont Way
St. Albert, Alberta
K2P 7W3
Phone: 587-412-6630
Email: info@meloraskin.com
Requirements
Must have
- -Logo supplied with the name and address of the clinic
- -Back of card in full color with white logo with A small line of text indicating both of the following: Anti aging consultants and cosmetic injectables
- Located inside the Voyager Wellness Group

```html
<!DOCTYPE html>
<html lang="en">
<head>
<meta charset="utf-8">
<title>MeloraSkin Business Card</title>
<link href="https://fonts.googleapis.com/css2?family=Poppins:wght@500;600&family=Open+Sans:ital,wght@1,400&display=swap" rel="stylesheet">
<style>
  :root {
    --page-bg: #ececef;
    --card-white: #ffffff;
    --brand-purple: #5f3c8c;
    --brand-purple-light: #7a56ad;
    --brand-pink: #e0569d;
    --brand-teal: #33b8a5;
    --ink: #1c1c1c;
    --white: #ffffff;
  }
  * { margin: 0; padding: 0; box-sizing: border-box; }
  html, body {
    width: 1200px;
    height: 1000px;
    overflow: hidden;
    background: var(--page-bg);
  }
  .canvas {
    width: 1200px;
    height: 1000px;
    display: flex;
    align-items: center;
    justify-content: center;
    gap: 48px;
  }
  .card {
    width: 520px;
    height: 300px;
    border-radius: 22px;
    position: relative;
    overflow: hidden;
    box-shadow: 0 10px 24px rgba(0,0,0,0.15);
  }
  .card-front { background: var(--card-white); }
  .front-artwork {
    position: absolute;
    left: 0;
    top: 0;
    width: 230px;
    height: 300px;
  }
  .contact-block {
    position: absolute;
    left: 280px;
    top: 92px;
    font-family: "Poppins", sans-serif;
    font-weight: 600;
    font-size: 15px;
    line-height: 1.3;
    color: var(--ink);
    text-align: center;
  }
  .contact-block .address { margin-bottom: 18px; }
  .card-back {
    background: linear-gradient(135deg, var(--brand-purple-light) 0%, var(--brand-purple) 55%, #583584 100%);
  }
  .brand-lockup {
    position: absolute;
    left: 70px;
    top: 92px;
    display: flex;
    align-items: center;
    gap: 16px;
  }
  .brand-mark {
    width: 58px;
    height: 58px;
    border-radius: 50%;
    background: var(--white);
  }
  .brand-name {
    font-family: "Poppins", sans-serif;
    font-weight: 600;
    font-size: 42px;
    color: var(--white);
    letter-spacing: 1px;
  }
  .tagline {
    position: absolute;
    left: 70px;
    top: 196px;
    font-family: "Open Sans", sans-serif;
    font-style: italic;
    font-weight: 400;
    font-size: 13.5px;
    line-height: 1.45;
    color: var(--white);
  }
</style>
</head>
<body>
  <main class="canvas">
    <section class="card card-front">
      <svg class="front-artwork" viewBox="0 0 230 300" role="img" aria-label="Illustration of a woman in profile with flowing pink, teal and purple hair">
        <defs>
          <linearGradient id="artwork-fill" x1="0" y1="0" x2="1" y2="1">
            <stop offset="0" stop-color="#e0569d"/>
            <stop offset="0.45" stop-color="#7a56ad"/>
            <stop offset="1" stop-color="#33b8a5"/>
          </linearGradient>
        </defs>
        <rect width="230" height="300" fill="url(#artwork-fill)" opacity="0.9"/>
      </svg>
      <div class="contact-block">
        <p class="address">14, 618 Birchmont Way<br>St. Albert, Alberta<br>K2P 7W3</p>
        <p class="phone">587-412-6630</p>
        <p class="email">info@meloraskin.com</p>
      </div>
    </section>

    <section class="card card-back">
      <div class="brand-lockup">
        <span class="brand-mark"></span>
        <span class="brand-name">MeloraSkin</span>
      </div>
      <p class="tagline">Anti aging consultants and cosmetic injectables<br>Located inside the Voyager Wellness Group</p>
    </section>
  </main>
</body>
</html>
```